the kobo bite

we have a product called the kobo bite that we are looking for a label for the packaging - it is a weight loss chocolate bar for men only
its a low sugar low calorie healthy snack
our website is www.thetorvablend.com.au for more info about our company.
looking for a label design thats manly but also for the everyday person to eat
Our company colurs are blue, yellow and white.
Looking for something a bit quirky that grabs peoples attention.

```html
<!DOCTYPE html>
<html lang="en">
<head>
<meta charset="utf-8">
<title>The Kobo Bite – Label</title>
<link rel="stylesheet" href="https://fonts.googleapis.com/css2?family=Oswald:wght@500;600;700&display=swap">
<style>
  :root {
    --page: #ffffff;
    --choc: #5a2d14;
    --choc-dark: #3f1d0b;
    --blue: #2a2fa0;
    --blue-deep: #1b1f7a;
    --stripe: #1c2186;
    --orange: #f5a11c;
    --orange-light: #ffc247;
    --white: #ffffff;
  }
  * { margin: 0; padding: 0; box-sizing: border-box; }
  html, body {
    width: 1200px; height: 1000px; overflow: hidden;
    background: var(--page);
  }
  .canvas { position: relative; width: 1200px; height: 1000px; }
  .label {
    position: absolute; left: 38px; top: 330px;
    width: 1124px; height: 338px; overflow: hidden;
  }
  .label-art { position: absolute; inset: 0; display: block; }
  .tagline {
    position: absolute; left: 38px; top: 12px;
    font-family: "Oswald", sans-serif; font-weight: 500;
    font-size: 33px; letter-spacing: 0.2px;
    color: var(--orange); text-transform: uppercase;
  }
  .product-name {
    position: absolute; left: 40px; top: 108px; width: 820px;
    text-align: center;
    font-family: "Oswald", sans-serif; font-weight: 700;
    font-size: 130px; line-height: 1;
    color: var(--orange);
  }
  .badge-text {
    position: absolute; left: 872px; top: 115px; width: 180px; height: 180px;
    display: flex; flex-direction: column; align-items: center; justify-content: center;
    text-align: center; color: var(--white);
    font-family: "Oswald", sans-serif; font-weight: 700;
    line-height: 1.05;
  }
  .badge-text .big { display: block; font-size: 40px; }
  .badge-text .small { display: block; font-size: 24px; font-weight: 600; }
</style>
</head>
<body>
<main class="canvas">
  <section class="label">
    <svg class="label-art" viewBox="0 0 1124 338" width="1124" height="338">
      <defs>
        <pattern id="panel-stripes" width="10" height="10" patternUnits="userSpaceOnUse">
          <rect width="10" height="10" fill="var(--blue)"/>
          <rect y="6" width="10" height="3" fill="var(--stripe)"/>
        </pattern>
        <radialGradient id="badge-fill" cx="50%" cy="45%" r="60%">
          <stop offset="0%" stop-color="var(--orange-light)"/>
          <stop offset="100%" stop-color="#ec7d12"/>
        </radialGradient>
        <linearGradient id="choc-fill" x1="0" y1="0" x2="0" y2="1">
          <stop offset="0%" stop-color="var(--choc-dark)"/>
          <stop offset="100%" stop-color="var(--choc)"/>
        </linearGradient>
      </defs>
      <rect class="panel" width="1124" height="338" fill="url(#panel-stripes)"/>
      <path class="choc-band" role="img" aria-label="Melted chocolate dripping over the top of the label"
            d="M0 0 H1124 V70 C 900 95, 600 60, 300 92 C 180 104, 80 90, 0 96 Z"
            fill="url(#choc-fill)"/>
      <path class="choc-edge" d="M0 300 C 300 318, 700 290, 1124 200 V338 H0 Z" fill="var(--choc)"/>
      <path class="orange-sweep" d="M0 312 C 300 330, 700 302, 1124 214 V338 H0 Z" fill="var(--orange)"/>
      <g class="badge" transform="translate(962 205)">
        <polygon fill="url(#badge-fill)" stroke="#ffd27a" stroke-width="3"
          points="90,0 75.3,20.2 77.9,45 55.2,55.2 45,77.9 20.2,75.3 0,90 -20.2,75.3 -45,77.9 -55.2,55.2 -77.9,45 -75.3,20.2 -90,0 -75.3,-20.2 -77.9,-45 -55.2,-55.2 -45,-77.9 -20.2,-75.3 0,-90 20.2,-75.3 45,-77.9 55.2,-55.2 77.9,-45 75.3,-20.2"/>
      </g>
    </svg>
    <p class="tagline">A weight loss chocolate bar for men</p>
    <h1 class="product-name">KOBO BITE</h1>
    <p class="badge-text">
      <span class="big">LOW</span>
      <span class="small">SUGAR</span>
      <span class="small">CALORIE</span>
    </p>
  </section>
</main>
</body>
</html>
```